Corrow Family Farm fresh honey jar label

I need a label for jars of honey harvested at our farm. These are for gifts and personal use. We are looking to incorporate our farm brand into the label. We would like the design to take the existing brand and add some element like bees, honey, flowers, or hives to indicate the contents. We want the design to feel homemade and authentic without feeling cheap or hoaky

Requirements
Must have
• The label must be made to fit a 1" x2" rectangular label. The label must include the attached family brand. The label must include the text "Corrow Family Farms" "Pinebrook, USA" "Farm Fresh Honey". The label will be printed on off-white paper
Nice to have
• It would be nice to have illustrations of bees or flowers around the logo or hives or honeycombs. The label should have a vintage feel
Should not have
• The label should not feel overly cartoonish or hoaky

```html
<!DOCTYPE html>
<html lang="en">
<head>
<meta charset="utf-8">
<title>Corrow Family Farms – Farm Fresh Honey Label</title>
<link rel="stylesheet" href="https://fonts.googleapis.com/css2?family=Amatic+SC:wght@400;700&family=Montserrat:wght@500;700&display=swap">
<style>
  :root {
    --page: #ffffff;
    --paper: #f7f1e6;
    --paper-edge: #e6cfa8;
    --ink: #111111;
    --art-light: #ece4d5;
    --art-dark: #ddd2bf;
  }
  html, body {
    margin: 0;
    padding: 0;
    width: 1200px;
    height: 1200px;
    overflow: hidden;
    background: var(--page);
  }
  .canvas {
    position: relative;
    width: 1200px;
    height: 1200px;
  }
  .label {
    position: absolute;
    left: 350px;
    top: 98px;
    width: 500px;
    height: 1004px;
    border-radius: 28px;
    background: var(--paper);
    box-shadow:
      inset 0 0 0 6px var(--paper-edge),
      inset 0 0 26px 10px rgba(230, 207, 168, 0.85),
      0 14px 24px rgba(0, 0, 0, 0.18);
    color: var(--ink);
    font-family: "Montserrat", Arial, sans-serif;
  }
  .brand-mark {
    position: absolute;
    top: 120px;
    left: 0;
    right: 0;
    text-align: center;
    font-weight: 700;
    font-size: 78px;
    letter-spacing: 4px;
    line-height: 1;
  }
  .brand-location {
    position: absolute;
    top: 280px;
    left: 0;
    right: 0;
    text-align: center;
    font-weight: 500;
    font-size: 15px;
    letter-spacing: 1px;
  }
  .art {
    position: absolute;
    border-radius: 6px;
    background: linear-gradient(180deg, var(--art-light), var(--art-dark));
  }
  .art--upper {
    left: 70px;
    top: 355px;
    width: 360px;
    height: 228px;
  }
  .art--lower {
    left: 120px;
    top: 694px;
    width: 260px;
    height: 96px;
  }
  .product-banner {
    position: absolute;
    left: 40px;
    top: 588px;
    width: 420px;
    height: 100px;
  }
  .product-banner svg {
    position: absolute;
    inset: 0;
  }
  .product-name {
    position: absolute;
    left: 0;
    right: 0;
    top: 14px;
    text-align: center;
    font-family: "Amatic SC", "Comic Sans MS", cursive;
    font-weight: 400;
    font-size: 64px;
    line-height: 1;
    letter-spacing: 1px;
  }
  .farm-name {
    position: absolute;
    top: 868px;
    left: 0;
    right: 0;
    text-align: center;
    font-weight: 700;
    font-size: 30px;
    letter-spacing: 1px;
  }
  .farm-location {
    position: absolute;
    top: 918px;
    left: 0;
    right: 0;
    text-align: center;
    font-weight: 500;
    font-size: 24px;
    letter-spacing: 1px;
  }
</style>
</head>
<body>
  <main class="canvas">
    <section class="label">
      <div class="brand-mark">CORROW</div>
      <div class="brand-location">PINEBROOK, LOUISIANA</div>

      <div class="art art--upper" role="img" aria-label="Vintage line illustration of a honeybee flying over wildflowers"></div>

      <div class="product-banner">
        <svg width="420" height="100" viewBox="0 0 420 100" aria-hidden="true">
          <line x1="0" y1="6" x2="420" y2="4" stroke="#111" stroke-width="2"/>
          <line x1="0" y1="94" x2="420" y2="96" stroke="#111" stroke-width="2"/>
        </svg>
        <div class="product-name">Farm Fresh Honey</div>
      </div>

      <div class="art art--lower" role="img" aria-label="Line illustration of flower stems and leaves below the banner"></div>

      <div class="farm-name">CORROW FAMILY FARMS</div>
      <div class="farm-location">PINEBROOK, USA</div>
    </section>
  </main>
</body>
</html>
```